Business Card Design for Law firm - already have logo

Now that we have a logo, we need a business card design - our logo is attached -it is salaryman font if that helps - we would like a file that can be uploaded to cardquill (www.cardquill-example.com) using the logo and with the following information on it:
Quenby Law Firm, P.C.
Delwyn Quenby, Esq.
5817 SW 19th Ave.
Alderton, OR 97990
971.555.0142 phone
971.555.0187 fax
del@quenby-example.net
Chat: delquenby
Google talk: delwyn.quenby@mailbox-example.com
Target Market(s)
our business cards are distributed to corporate executives, technology professionals and healthcare providers
Industry/Entity Type
Business
Look and feel

```html
<!DOCTYPE html>
<html lang="en">
<head>
<meta charset="utf-8">
<title>Quenby Law Firm – Business Card</title>
<link rel="stylesheet" href="https://fonts.googleapis.com/css2?family=Questrial&display=swap">
<style>
  :root {
    --backdrop-light: #8aa88a;
    --backdrop-dark: #2f7a32;
    --card-light: #b4b4b4;
    --card-dark: #8c8c8c;
    --strip-dark: #3a3a3a;
    --strip-mid: #6b6b6b;
    --stripe-light: #c4c4c4;
    --stripe-dark: #2e2e2e;
    --text-light: #f4f4f4;
    --wordmark: #4a4a4a;
  }
  * { box-sizing: border-box; margin: 0; padding: 0; }
  html, body { width: 1200px; height: 699px; overflow: hidden; }
  body {
    position: relative;
    font-family: "Questrial", "Century Gothic", sans-serif;
    background: radial-gradient(ellipse 75% 85% at 40% 45%, var(--backdrop-light) 0%, #5f8f60 55%, var(--backdrop-dark) 100%);
  }
  .card {
    position: absolute;
    overflow: hidden;
    box-shadow: 6px 6px 8px rgba(0,0,0,0.35);
  }
  .card--front {
    left: 12px; top: 43px; width: 512px; height: 286px;
    background: linear-gradient(160deg, #c2c2c2 0%, var(--card-light) 40%, #9e9e9e 100%);
  }
  .card--back {
    left: 551px; top: 323px; width: 624px; height: 349px;
    background: linear-gradient(200deg, #c8c8c8 0%, #a6a6a6 45%, var(--card-dark) 100%);
  }
  .strip { position: absolute; top: 0; bottom: 0; }
  .card--front .strip--wide { left: 0; width: 51px; background: var(--strip-dark); }
  .card--front .stripe--light { left: 51px; width: 15px; background: var(--stripe-light); }
  .card--front .stripe--dark { left: 66px; width: 12px; background: var(--stripe-dark); }
  .card--back .strip--wide { left: 0; width: 76px; background: var(--strip-mid); }
  .card--back .stripe--light { left: 76px; width: 7px; background: var(--stripe-light); }
  .card--back .stripe--dark { left: 83px; width: 17px; background: var(--strip-mid); filter: brightness(0.85); }

  .wordmark {
    position: absolute;
    color: var(--wordmark);
    letter-spacing: 0.55em;
    line-height: 1;
    white-space: nowrap;
  }
  .card--front .wordmark { left: 290px; top: 144px; font-size: 26px; }
  .card--back .wordmark { left: 356px; top: 172px; font-size: 32px; }

  .label, .detail {
    position: absolute;
    color: var(--text-light);
    font-size: 14px;
    line-height: 18px;
    white-space: nowrap;
  }
  .label { left: 12px; }
  .detail { left: 116px; }
  .icon {
    position: absolute;
    left: 82px;
    width: 16px; height: 16px;
  }
  .icon svg { width: 100%; height: 100%; fill: var(--text-light); }
</style>
</head>
<body>

<section class="card card--front" aria-label="Card front">
  <div class="strip strip--wide"></div>
  <div class="strip stripe--light"></div>
  <div class="strip stripe--dark"></div>
  <div class="wordmark">QUENBY</div>
</section>

<section class="card card--back" aria-label="Card back">
  <div class="strip strip--wide"></div>
  <div class="strip stripe--light"></div>
  <div class="strip stripe--dark"></div>

  <span class="icon" style="top:62px"><svg viewBox="0 0 16 16"><circle cx="8" cy="5" r="3.5"/><path d="M1 16c0-4 3-6.5 7-6.5s7 2.5 7 6.5z"/></svg></span>
  <span class="detail" style="top:62px">Quenby Law Firm, P.C.</span>

  <span class="label" style="top:98px">Adress</span>
  <span class="icon" style="top:99px"><svg viewBox="0 0 16 16"><path d="M8 1 0 8h2v7h4v-4h4v4h4V8h2z"/></svg></span>
  <span class="detail" style="top:99px">Delwyn Quenby, Esq.</span>
  <span class="detail" style="top:117px">5817 SW 19th Ave.</span>
  <span class="detail" style="top:135px">Alderton, OR 97990</span>

  <span class="label" style="top:171px">Phone</span>
  <span class="icon" style="top:172px"><svg viewBox="0 0 16 16"><path d="M5 1c-2 1-3 3-3 7s1 6 3 7l2-3-2-2c-.5-1.3-.5-2.7 0-4l2-2z"/></svg></span>
  <span class="detail" style="top:172px">971.555.0142</span>

  <span class="label" style="top:190px">Fax</span>
  <span class="icon" style="top:191px"><svg viewBox="0 0 16 16"><rect x="4" y="1" width="8" height="5"/><rect x="2" y="6" width="12" height="9" rx="1"/></svg></span>
  <span class="detail" style="top:190px">971.555.0187</span>

  <span class="label" style="top:210px">web Site</span>
  <span class="detail" style="top:208px">del@quenby-example.net</span>

  <span class="label" style="top:227px">Chat</span>
  <span class="icon" style="top:227px"><svg viewBox="0 0 16 16"><circle cx="8" cy="8" r="7"/></svg></span>
  <span class="detail" style="top:226px">delquenby</span>

  <span class="label" style="top:245px">IM</span>
  <span class="icon" style="top:246px"><svg viewBox="0 0 16 16"><circle cx="8" cy="8" r="7"/></svg></span>
  <span class="detail" style="top:245px">delwyn.quenby@mailbox-example.com</span>

  <div class="wordmark">QUENBY</div>
</section>

</body>
</html>
```